Non-profit sports organization needs templates for Word and InDesign

"Fralo Teens" is a non-profit organization in Winterthur, which supports the recruitment of young talent by the handball clubs in Winterthur. Every year we run several camps, a tournament for schoolchildren and several handball lessons at school.
During these activities there are always written information. So far we have not given much thought to the design. But since we think that a professional design will also lead to more interaction, we now turn to you as a designer.

For the communication with partners, sponsors, patrons, etc. we need a uniform appearance. Since different departments are currently working with different programs, we need a template for letters and documentation for Word and InDesign.

We will need the documentation template for project descriptions, information, etc.
The letter templates are needed to contact sponsors, authorities, patrons, etc.

Both the letter template and the documentation template should look modern. The design should be based on the existing flyers. Otherwise we have no other requirements so far.

Homepage: www.fralo-teens.ch

Target Market(s)

Letters, documentation or information to authorities, sponsors, associations, patrons, members, participants, etc.

Requirements
Must have
• In addition to the design, the templates should also contain a concept for titles, paragraphs, lists, etc. (colors / fonts / ...)

Word and Indesign templates

```html
<!DOCTYPE html>
<html lang="en">
<head>
<meta charset="utf-8">
<title>Fralo Teens – Letterhead</title>
<link rel="stylesheet" href="https://fonts.googleapis.com/css2?family=Barlow:wght@500;600&display=swap">
<style>
  :root {
    --blue: #27a0dc;
    --red: #f29593;
    --pink: #f9c8c9;
    --grey: #d9d9d9;
    --grey-light: #e3e3e3;
    --ink: #111111;
    --paper: #ffffff;
  }
  html, body {
    margin: 0;
    padding: 0;
    overflow: hidden;
    background: var(--paper);
  }
  .letterhead {
    position: relative;
    width: 849px;
    height: 1200px;
    overflow: hidden;
    background: var(--paper);
    font-family: "Barlow", sans-serif;
  }
  .letterhead__graphics {
    position: absolute;
    inset: 0;
    width: 849px;
    height: 1200px;
  }
  .brand-name {
    position: absolute;
    left: 66px;
    top: 128px;
    margin: 0;
    font-size: 38px;
    font-weight: 600;
    color: var(--blue);
    letter-spacing: 0.5px;
  }
  .website {
    position: absolute;
    left: 87px;
    top: 1158px;
    font-size: 22px;
    font-weight: 500;
    color: var(--paper);
    letter-spacing: 1px;
  }
  .sponsors__label {
    position: absolute;
    left: 384px;
    top: 1094px;
    margin: 0;
    font-size: 20px;
    font-weight: 600;
    color: var(--ink);
  }
  .sponsors__list {
    position: absolute;
    left: 380px;
    top: 1152px;
    width: 436px;
    margin: 0;
    padding: 0;
    list-style: none;
    display: flex;
    justify-content: space-between;
    align-items: center;
  }
  .sponsor {
    font-size: 13px;
    font-weight: 600;
    color: var(--ink);
    white-space: nowrap;
  }
</style>
</head>
<body>
<main class="letterhead">
  <svg class="letterhead__graphics" viewBox="0 0 1624 2296" preserveAspectRatio="none" aria-hidden="true">
    <rect class="band-grey" x="0" y="0" width="1624" height="126" fill="var(--grey)"/>
    <polygon class="band-red" points="640,116 1624,116 1624,155 1545,293 1515,347 511,347" fill="var(--red)"/>
    <polygon class="band-pink" points="1282,293 1545,293 1515,347 1253,347" fill="var(--pink)"/>
    <polygon class="band-blue" points="535,0 1540,0 1410,231 407,231" fill="var(--blue)" opacity="0.5"/>

    <polygon class="foot-pink" points="0,1903 299,1903 170,2133 0,2133" fill="var(--red)" opacity="0.5"/>
    <polygon class="foot-blue-light" points="0,2019 403,2019 360,2097 0,2097" fill="var(--blue)" opacity="0.25"/>
    <polygon class="foot-blue" points="0,2097 360,2097 318,2172 135,2172 90,2250 0,2250" fill="var(--blue)" opacity="0.5"/>

    <polygon class="foot-frame" points="693,2055 1624,2055 1624,2296 70,2296 135,2172 628,2172" fill="var(--grey-light)"/>
    <polygon class="foot-panel" points="705,2073 1624,2073 1624,2296 580,2296 645,2180" fill="var(--paper)"/>
    <polygon class="foot-url-bar" points="143,2180 645,2180 580,2296 78,2296" fill="var(--ink)"/>
  </svg>

  <h1 class="brand-name">Fralo Teens</h1>

  <span class="website">www.fralo-teens.ch</span>

  <section class="sponsors">
    <h2 class="sponsors__label">Sponsored by</h2>
    <ul class="sponsors__list">
      <li class="sponsor">Dr. Berling Ostmann</li>
      <li class="sponsor">Nordsports</li>
      <li class="sponsor">Kramerhaus</li>
      <li class="sponsor">Sportverband Region</li>
    </ul>
  </section>
</main>
</body>
</html>
```